Yumm... Caramel packaging

We want to create a derivative of our gummies packaging for our new product, our chewable caramel. We would like to use a caramel, brownish, cream pallet. With hints of green. See example1.pdf for an example of the colors, they DO NOT have to be exact. Check YUMM Dulce de Leche.psd for the logo with approximated colors, you can change these, but please keep logo structure. 3.62x4.50x1.50.pdf is the guideline for the packaging print, this includes size and print area. All Gummies Mock up.jpg is our gummies packaging line up, mocked up. All warnings must be included, use this as guide.

Designers are asking for more time, and i want higher quiality submissions.

```html
<!DOCTYPE html>
<html lang="en">
<head>
<meta charset="utf-8">
<title>Yumm... Caramel Chew Pouch</title>
<link rel="stylesheet" href="https://fonts.googleapis.com/css2?family=Bebas+Neue&family=Montserrat:wght@800&family=Roboto+Condensed:wght@700&display=swap">
<style>
  :root {
    --page: #ffffff;
    --foil-light: #ececec;
    --foil-dark: #cbcbcb;
    --cream-light: #e4dbb1;
    --cream-dark: #c4b88a;
    --ink: #111111;
    --brand-ink: #333333;
    --leaf-green: #2e5e3a;
    --pill-rim: #c3d394;
    --pill-top: #6f9a44;
    --pill-bottom: #1f6a30;
    --label-cream: #ebe4c4;
    --label-rim: #d9b77c;
    --caramel-light: #e39a3a;
    --caramel-dark: #b8581c;
    --sticker-grey: #7a7a7a;
    --badge: #000000;
  }
  * { margin: 0; padding: 0; box-sizing: border-box; }
  html, body { width: 809px; height: 1200px; overflow: hidden; background: var(--page); }
  .canvas { position: relative; width: 809px; height: 1200px; }

  .pouch {
    position: absolute; left: 132px; top: 107px; width: 562px; height: 917px;
    border-radius: 26px; overflow: hidden;
    background: linear-gradient(180deg, var(--foil-light), var(--foil-dark));
  }
  .pouch-cream {
    position: absolute; left: 366px; top: 0; width: 196px; height: 100%;
    background: linear-gradient(180deg, var(--cream-light), var(--cream-dark));
  }

  .brand {
    position: absolute; left: 348px; top: 526px;
    transform: translate(-50%, -50%) rotate(-90deg);
    font-family: "Montserrat", sans-serif; font-weight: 800;
    font-size: 84px; line-height: 1; color: var(--brand-ink);
    white-space: nowrap;
  }
  .brand-dot {
    position: absolute; left: 363px; top: 359px; width: 16px; height: 16px;
    border-radius: 50%; background: var(--leaf-green);
  }

  .flavour-pill {
    position: absolute; left: 426px; top: 361px; width: 153px; height: 385px;
    border-radius: 77px; padding: 4px;
    background: var(--pill-rim);
  }
  .flavour-pill-inner {
    position: relative; width: 100%; height: 100%; border-radius: 73px; overflow: hidden;
    background: linear-gradient(180deg, var(--pill-top) 0%, #86a45a 45%, var(--pill-bottom) 100%);
  }
  .flavour-label {
    position: absolute; left: 10px; top: 10px; width: 133px; height: 133px;
    border-radius: 50%; background: var(--label-cream);
    border: 3px solid var(--label-rim);
    box-shadow: 0 6px 10px rgba(0,0,0,0.25);
    display: flex; align-items: center; justify-content: center; text-align: center;
    font-family: "Bebas Neue", sans-serif; font-size: 34px; line-height: 0.95;
    color: var(--ink);
  }
  .caramel-visual {
    position: absolute; left: 0; top: 182px; width: 100%; height: 175px;
    background: linear-gradient(160deg, var(--caramel-light), var(--caramel-dark));
    border-radius: 0 0 40px 30px;
  }

  .sticker-area {
    position: absolute; left: 206px; top: 770px; width: 228px; height: 113px;
    border: 1px dashed #444;
  }
  .sticker-fields {
    position: absolute; left: 10px; top: 20px;
    font-family: "Roboto Condensed", sans-serif; font-weight: 700;
    font-size: 18px; line-height: 23.5px; color: var(--ink); letter-spacing: 0.5px;
  }
  .sticker-hint {
    position: absolute; left: 116px; top: 33px; width: 100px; text-align: center;
    font-family: "Roboto Condensed", sans-serif; font-weight: 700;
    font-size: 17px; line-height: 23px; color: var(--sticker-grey); letter-spacing: 0.5px;
  }

  .cert-badge {
    position: absolute; left: 533px; top: 786px; width: 72px; height: 72px;
    border-radius: 50%; background: var(--badge);
  }

  .warning {
    position: absolute; left: 132px; top: 909px; width: 562px; text-align: center;
    font-family: "Roboto Condensed", sans-serif; font-weight: 700;
    font-size: 16.5px; line-height: 22px; color: var(--ink); letter-spacing: 0.4px;
  }
</style>
</head>
<body>
<main class="canvas">
  <section class="pouch">
    <div class="pouch-cream"></div>
  </section>

  <div class="brand">Yumm</div>
  <div class="brand-dot"></div>

  <div class="flavour-pill">
    <div class="flavour-pill-inner">
      <div class="flavour-label">CARAMEL<br>CHEW</div>
      <div class="caramel-visual" role="img" aria-label="Illustration of glossy caramel chew cubes in a pool of caramel sauce"></div>
    </div>
  </div>

  <div class="sticker-area">
    <div class="sticker-fields">POTENCY:<br>FLAVORS:<br>PIECES:</div>
    <div class="sticker-hint">STICKER<br>AREA</div>
  </div>

  <div class="cert-badge" role="img" aria-label="Certification badge"></div>

  <p class="warning">Contains Medical Cannabis. This product complies with all<br>mandatory contaminant testing.&nbsp; Keep out of reach of children.</p>
</main>
</body>
</html>
```